Lanterne architecture business cards

We are a new company based in New Zealand. We Specialize in High end Luxury Residential Architecture.

Every home is bespoke and is designed to each clients individual requirements and needs.

I like to design buildings that inspire people through light and form while offering a high level of comfort and usability.

Lines of sight, proportion and balance are fundamental to the spaces I create.
Updates

August 5th is current deadline - Today's date is the 13th of August.

Target Market(s)

New Zealanders who want a custom individual home design, typically 30-65 year old males and females

Industry/Entity Type

Architecture

Contact Information for Business Card

Director - Derek Tolson
Contact Number - 0279164073
Email - info@lanternearchitecture-example.co.nz
Webstie - www.lanternearchitecture-example.co.nz
Social Media - @lanternearchitecture

Font styles to use
Sans Serif

Requirements
Must have
• Logo (Both Sides)
Website
Email
Contact Number
Social Media

Nice to have
• Texture
Should not have
• More than 3 colours - typically I would've thought 2 would be good to match the logo.

```html
<!DOCTYPE html>
<html lang="en">
<head>
<meta charset="utf-8">
<title>Lanterne Architecture — Business Cards</title>
<link rel="stylesheet" href="https://fonts.googleapis.com/css2?family=Josefin+Sans:wght@300&family=Zilla+Slab:wght@400;500&display=swap">
<style>
  :root {
    --stage: #f3f3f3;
    --forest: #3d5a45;
    --paper: #f1f0ec;
    --ink: #1c1c1c;
    --ink-soft: #5a5a5a;
    --on-forest: #f4f4f0;
    --plan-light: rgba(255, 255, 255, 0.07);
    --plan-dark: rgba(60, 60, 60, 0.07);
  }
  * { margin: 0; padding: 0; box-sizing: border-box; }
  html, body {
    width: 1200px;
    height: 1200px;
    overflow: hidden;
    background: var(--stage);
  }
  .card {
    position: absolute;
    left: 208px;
    width: 767px;
    height: 446px;
    overflow: hidden;
  }
  .card--front { top: 109px; background: var(--forest); }
  .card--back { top: 620px; background: var(--paper); }

  .plan-area { position: absolute; }
  .card--front .plan-area {
    left: 582px; top: 172px; width: 185px; height: 274px;
    background: linear-gradient(160deg, rgba(255,255,255,0) 0%, var(--plan-light) 60%, rgba(255,255,255,0.03) 100%);
  }
  .card--back .plan-area {
    left: 362px; top: 20px; width: 330px; height: 420px;
    background: radial-gradient(ellipse at 55% 50%, var(--plan-dark) 0%, rgba(60,60,60,0.02) 70%, rgba(60,60,60,0) 100%);
  }

  .wordmark {
    position: absolute;
    font-family: "Josefin Sans", sans-serif;
    font-weight: 300;
    text-transform: uppercase;
    text-align: center;
    white-space: nowrap;
  }
  .wordmark__name, .wordmark__sub { display: block; }

  .card--front .wordmark {
    left: 0; width: 100%; top: 232px;
    color: var(--on-forest);
  }
  .card--front .wordmark__name {
    font-size: 36px; letter-spacing: 0.52em; padding-left: 0.52em;
  }
  .card--front .wordmark__sub {
    margin-top: 6px; font-size: 11px; letter-spacing: 0.95em; padding-left: 0.95em;
  }

  .card--back .wordmark {
    left: 500px; width: 260px; top: 382px;
    color: var(--ink);
  }
  .card--back .wordmark__name {
    font-size: 21px; letter-spacing: 0.5em; padding-left: 0.5em;
  }
  .card--back .wordmark__sub {
    margin-top: 2px; font-size: 7px; letter-spacing: 1em; padding-left: 1em;
  }

  .contact-bar {
    position: absolute; left: 0; top: 88px; width: 5px; height: 89px;
    background: var(--ink);
  }
  .contact-list {
    position: absolute; left: 38px; top: 86px;
    list-style: none;
    font-family: "Zilla Slab", serif;
    font-size: 13.5px;
    color: var(--ink);
    letter-spacing: 0.05em;
  }
  .contact-list li { display: flex; height: 24.6px; align-items: center; }
  .contact-label { width: 38px; font-size: 11px; letter-spacing: 0.25em; color: var(--ink-soft); }

  .person { position: absolute; left: 39px; top: 344px; font-family: "Zilla Slab", serif; }
  .person__name {
    font-size: 26px; font-weight: 500; letter-spacing: 0.1em; color: var(--ink);
    text-transform: uppercase;
  }
  .person__role {
    margin-top: 1px; font-size: 12px; letter-spacing: 0.18em; color: var(--ink-soft);
    text-transform: uppercase;
  }
</style>
</head>
<body>
  <section class="card card--front" aria-label="Card front">
    <div class="plan-area" role="img" aria-label="Faint architectural floor plan drawing"></div>
    <div class="wordmark">
      <span class="wordmark__name">Lanterne</span>
      <span class="wordmark__sub">Architecture</span>
    </div>
  </section>

  <section class="card card--back" aria-label="Card back">
    <div class="plan-area" role="img" aria-label="Faint architectural floor plan drawing"></div>
    <div class="contact-bar"></div>
    <ul class="contact-list">
      <li><span class="contact-label">P :</span>0279164073</li>
      <li><span class="contact-label">E :</span>info@lanternearchitecture-example.co.nz</li>
      <li><span class="contact-label">W :</span>www.lanternearchitecture-example.co.nz</li>
      <li><span class="contact-label">S :</span>@lanternearchitecture</li>
    </ul>
    <div class="person">
      <p class="person__name">Derek Tolson</p>
      <p class="person__role">Director</p>
    </div>
    <div class="wordmark">
      <span class="wordmark__name">Lanterne</span>
      <span class="wordmark__sub">Architecture</span>
    </div>
  </section>
</body>
</html>
```